K48 PowerPoint Presentation

As you can see the design of this PowerPoint isn't cohesive. There are a lot of images and words that give it a very jumbled and busy appeal. We want to turn this into a sharp, cohesive and visually appealing presentation without taking away too much of the information. Feel free to use the images to create your own artwork for the PowerPoint.

Please don't hesitate to contact me with any questions.

Industry/Entity Type

Graphic Design

```html
<!DOCTYPE html>
<html lang="en">
<head>
<meta charset="utf-8">
<title>K48 Presentation Slides</title>
<link rel="stylesheet" href="https://fonts.googleapis.com/css2?family=Open+Sans:wght@300;400;600;700&display=swap">
<style>
:root{
  --navy:#2c4a6e;
  --deep:#1f3957;
  --steel:#4a7fa0;
  --sky:#5fa3c4;
  --ice:#a9d2e4;
  --orange:#f47a30;
  --ink:#3a3a3a;
  --muted:#8a8a8a;
  --rule:#dcdcdc;
}
*{margin:0;padding:0;box-sizing:border-box}
html,body{width:1200px;height:1088px;overflow:hidden}
body{font-family:"Open Sans",Arial,sans-serif;color:var(--ink);
  background:radial-gradient(ellipse at 50% 45%,#eeeeee 0%,#d6d6d6 55%,#bdbdbd 100%);position:relative}
.slide{position:absolute;background:#fff;overflow:hidden;box-shadow:0 1px 4px rgba(0,0,0,.3)}
.big{width:368px;height:200px}
.small{width:262px;height:148px}
.head{position:absolute;left:0;right:0;top:0;height:26px;border-bottom:1px solid var(--rule);text-align:center;font-size:9px;line-height:27px;color:var(--navy);letter-spacing:.4px;font-weight:400;background:#fff}
.small .head{height:20px;line-height:21px;font-size:6.5px}
.head em{font-style:normal;color:var(--sky)}
.foot{position:absolute;left:0;right:0;bottom:0;height:12px;background:var(--navy)}
.small .foot{height:9px}
.foot i{position:absolute;top:3.5px;width:5px;height:5px;background:#fff}
.small .foot i{top:2.5px;width:4px;height:4px}
.foot i:nth-child(1){left:8px}.foot i:nth-child(2){left:15px}.foot i:nth-child(3){left:22px}
.small .foot i:nth-child(2){left:14px}.small .foot i:nth-child(3){left:20px}
.foot span{position:absolute;left:0;right:0;text-align:center;font-size:4px;line-height:12px;color:#fff}
.small .foot span{font-size:3.4px;line-height:9px}
.blue{position:absolute;left:0;right:0;top:26px;bottom:12px;background:linear-gradient(180deg,#3b6789 0%,#6fa8c5 45%,#3c6a8c 75%,#27496b 100%)}
.ph{position:absolute;background:linear-gradient(135deg,#d9dee3,#9fb1c0)}
.ph.dark{background:linear-gradient(135deg,#6c7b66,#3b4c5c)}
.ph.warm{background:linear-gradient(135deg,#c9b48a,#6d5a44)}
.ph.device{background:linear-gradient(160deg,#f1f3f5 0%,#cfd6dd 60%,#9aa6b2 100%)}
.tiny{position:absolute;font-size:3.4px;line-height:4.4px;color:#777}
.tiny.w{color:#eaf3f8}
.pointer{position:absolute;left:0;height:1px;background:var(--steel)}
.pointer::after{content:"";position:absolute;right:-2px;top:-1.5px;width:4px;height:4px;border-radius:50%;background:var(--steel)}
.lead{position:absolute;font-size:5px;color:var(--navy)}
.lead b{color:var(--orange);font-weight:600}
.o{color:var(--orange)}
.s{color:var(--sky)}
.list{position:absolute;list-style:none;font-size:4px;line-height:6.6px;color:#555}
.list.w{color:#fff}
.list li::before{content:"• ";color:var(--steel)}
.list.w li::before{color:#fff}
.num{position:absolute;width:12px;height:12px;border-radius:50%;border:1px solid #fff;color:#fff;font-size:5px;text-align:center;line-height:10px}
.cap{position:absolute;font-size:3.8px;color:#fff;font-weight:600;text-align:center}
.screen{position:absolute;background:#1e2a36;border-radius:1px;padding:1.5px}
.screen .ph{left:1.5px;top:1.5px;right:1.5px;bottom:1.5px}
.lbl{position:absolute;font-size:3.8px;color:#fff;text-align:center}
.dot{position:absolute;width:6px;height:6px;border-radius:50%;background:var(--orange)}
.row{position:absolute;left:205px;width:152px;height:11px;background:#eef2f5;font-size:3.8px;line-height:11px;color:#555}
.row b{display:inline-block;width:14px;height:11px;background:var(--sky);color:#fff;text-align:center;margin-right:5px;font-weight:600}
.row.sub{left:225px;width:132px;background:#f6f6f6}
.row.sub b{background:var(--steel);width:10px}
.note{position:absolute;background:#eee;font-size:3.4px;line-height:4.4px;color:#666;padding:2px 3px 2px 14px}
.note::before{content:"";position:absolute;left:3px;top:2px;width:8px;height:8px;border-radius:50%;background:var(--orange)}
.band{position:absolute;left:0;top:698px;width:1200px;height:21px;background:var(--navy)}
.circ{position:absolute;border-radius:50%;color:#fff;text-align:center;display:flex;align-items:center;justify-content:center}
.brand{position:absolute;left:935px;top:945px;display:flex;align-items:center;gap:14px}
.brand .mark{width:54px;height:54px;border-radius:50%;background:var(--steel)}
.brand .name{font-size:46px;font-weight:700;color:var(--navy);letter-spacing:1px}
</style>
</head>
<body>

<!-- Row 1 -->
<section class="slide big" style="left:26px;top:32px">
  <h2 class="head">IDEAS <em>TO</em> REALITY</h2>
  <div class="pointer" style="top:48px;width:62px"></div>
  <p class="lead" style="left:70px;top:45px">A <b>web-based</b> environment for architecture <b>decision analytics</b></p>
  <svg style="position:absolute;left:56px;top:68px" width="268" height="38" viewBox="0 0 268 38">
    <polygon points="0,0 80,0 92,18 80,36 0,36" fill="#5fa3c4"/>
    <polygon points="86,0 166,0 178,18 166,36 86,36 98,18" fill="#2c4a6e"/>
    <polygon points="172,0 252,0 264,18 252,36 172,36 184,18" fill="#f47a30"/>
    <circle cx="46" cy="13" r="4" fill="#fff"/><circle cx="132" cy="13" r="4" fill="#fff"/><circle cx="218" cy="13" r="4" fill="#fff"/>
    <text x="46" y="29" font-size="4.5" fill="#fff" text-anchor="middle" font-family="Open Sans">THE CHALLENGE</text>
    <text x="132" y="29" font-size="4.5" fill="#fff" text-anchor="middle" font-family="Open Sans">THE WAY</text>
    <text x="218" y="29" font-size="4.5" fill="#fff" text-anchor="middle" font-family="Open Sans">THE RESULT</text>
  </svg>
  <p class="tiny" style="left:60px;top:114px;width:72px;border-right:1px solid var(--rule);padding-right:6px">Identifying and integrating the sources of record across the organisation and making it <span class="o">quickly available</span> to decision makers.</p>
  <p class="tiny" style="left:142px;top:114px;width:72px;border-right:1px solid var(--rule);padding-right:6px">A portal system enabling the <span class="o">rapid alignment</span>, integration, display and analysis of data from multiple sources.</p>
  <p class="tiny" style="left:226px;top:114px;width:80px">A <span class="o">collaborative</span> architecture decision support tool that drives cost and guidance for mission impact.</p>
  <div class="foot"><i></i><i></i><i></i><span>Ideas to Reality 2014</span></div>
</section>

<section class="slide big" style="left:411px;top:32px">
  <h2 class="head">THE <em>BENIFITS</em></h2>
  <div class="pointer" style="top:40px;width:40px"></div>
  <p class="lead" style="left:48px;top:37px">A collaborative, web-based environment that provides an organisation with:</p>
  <ul class="list" style="left:22px;top:66px;width:120px;line-height:7.5px">
    <li>Strategic <span class="o">Planning</span> support</li>
    <li>Organizational alignment and <span class="o">Traceability</span> to strategic objectives</li>
    <li>Identification &amp; management of potential gaps</li>
    <li>Analysis of systems and functional <span class="o">Relationships</span></li>
    <li>The development and management of program <span class="o">Plans</span></li>
    <li>Supports the identification of current Requirements</li>
    <li><span class="o">Mission</span> support</li>
  </ul>
  <div class="ph" role="img" aria-label="Layered architecture diagram linking strategic direction, information flow and resources" style="left:150px;top:50px;width:200px;height:130px;background:linear-gradient(180deg,#f7c9a6 0%,#b9d7e8 40%,#9fc1d8 70%,#8da4bd 100%)"></div>
  <div class="foot"><i></i><i></i><i></i><span>Ideas to Reality 2014</span></div>
</section>

<section class="slide big" style="left:796px;top:32px">
  <h2 class="head">INSERT <em>HERE</em></h2>
  <div class="blue">
    <span class="num" style="left:28px;top:4px">1</span>
    <p class="cap" style="left:6px;top:18px;width:58px">ARCHITECTURE FRONT END</p>
    <p class="tiny w" style="left:6px;top:24px;width:58px;text-align:center">Lorem ipsum dolor sit amet, consectetur adipiscing elit, sed do eiusmod tempor.</p>
    <div class="screen" style="left:70px;top:8px;width:62px;height:44px"><div class="ph" role="img" aria-label="Dashboard screen with coloured bar charts"></div></div>
    <span class="num" style="left:165px;top:4px">2</span>
    <p class="cap" style="left:142px;top:18px;width:58px">EASY TO DISSEMINATE DATA</p>
    <p class="tiny w" style="left:142px;top:24px;width:58px;text-align:center">Lorem ipsum dolor sit amet, consectetur adipiscing elit, sed do eiusmod tempor.</p>
    <div class="screen" style="left:206px;top:8px;width:62px;height:44px"><div class="ph" role="img" aria-label="Dashboard screen with charts"></div></div>
    <span class="num" style="left:312px;top:4px">3</span>
    <p class="cap" style="left:282px;top:18px;width:72px">UNLIMITED EVALUATION OPTIONS</p>
    <p class="tiny w" style="left:282px;top:24px;width:72px;text-align:center">Lorem ipsum dolor sit amet, consectetur adipiscing elit, sed do eiusmod tempor.</p>
    <div style="position:absolute;left:0;right:0;top:66px;height:16px;background:rgba(255,255,255,.14)"></div>
    <div class="screen" style="left:6px;top:92px;width:54px;height:40px"><div class="ph" role="img" aria-label="Map view screen"></div></div>
    <span class="num" style="left:88px;top:90px">4</span>
    <p class="cap" style="left:64px;top:104px;width:62px">INTEGRATION FOR ALL SYSTEMS</p>
    <p class="tiny w" style="left:64px;top:110px;width:62px;text-align:center">Lorem ipsum dolor sit amet, consectetur adipiscing elit, sed do eiusmod tempor.</p>
    <div class="screen" style="left:134px;top:92px;width:54px;height:40px"><div class="ph" role="img" aria-label="Report screen"></div></div>
    <div class="screen" style="left:194px;top:92px;width:54px;height:40px"><div class="ph" role="img" aria-label="Chart screen"></div></div>
    <span class="num" style="left:274px;top:90px">5</span>
    <p class="cap" style="left:252px;top:104px;width:58px">CUSTOMIZABLE</p>
    <p class="tiny w" style="left:252px;top:110px;width:58px;text-align:center">Lorem ipsum dolor sit amet, consectetur adipiscing elit, sed do eiusmod tempor.</p>
    <div class="screen" style="left:314px;top:92px;width:48px;height:40px"><div class="ph" role="img" aria-label="Data table screen"></div></div>
  </div>
  <div class="foot"><i></i><i></i><i></i><span>Ideas to Reality 2014</span></div>
</section>

<!-- Row 2 -->
<section class="slide big" style="left:26px;top:250px">
  <h2 class="head">THE <em>PROCESS</em></h2>
  <div class="pointer" style="top:42px;width:16px"></div>
  <p class="lead" style="left:22px;top:39px;color:var(--sky)">K48 PROVIDES DATA INTEGRATION:</p>
  <ul class="list" style="left:26px;top:48px;width:110px;line-height:5.6px;font-size:3.6px">
    <li><span class="o">Integrates</span> data feeds from internal sources</li>
    <li><span class="o">Updates</span> can be made at any point of the cycle</li>
    <li>Changes to any data component ripple through</li>
    <li>Updates take effect <span class="o">immediately</span></li>
    <li>Provides the most <span class="o">current</span> data available</li>
    <li>Makes data analysis more accessible</li>
  </ul>
  <div class="pointer" style="top:97px;width:16px"></div>
  <p class="lead" style="left:22px;top:94px;color:var(--sky)">K48 DESIGN ALLOWS ORGANISATIONS TO:</p>
  <ul class="list" style="left:26px;top:103px;width:110px;line-height:5.6px;font-size:3.6px">
    <li>Justify programs</li>
    <li>Show decision impact</li>
    <li>Display <span class="o">traceability</span> to strategy</li>
    <li>Link to individual level</li>
    <li>Include <span class="o">priority</span> evaluations</li>
    <li>Include all possible options</li>
    <li>Maintain current requirements</li>
  </ul>
  <svg style="position:absolute;left:205px;top:40px" width="140" height="140" viewBox="-70 -70 140 140">
    <polygon points="0,-52 9,-15.6 45,-26 18,0 45,26 9,15.6 0,52 -9,15.6 -45,26 -18,0 -45,-26 -9,-15.6" fill="#3f6f93"/>
    <polygon points="0,-30 6,-6 30,0 6,6 0,30 -6,6 -30,0 -6,-6" fill="#4a7fa0" opacity=".7"/>
    <text y="-1" font-size="4.2" fill="#fff" text-anchor="middle" font-family="Open Sans">K48 Supported</text>
    <text y="4" font-size="4.2" fill="#fff" text-anchor="middle" font-family="Open Sans">Decision Cycle</text>
    <text y="-62" font-size="4" fill="#333" text-anchor="middle" font-family="Open Sans">Capability</text>
    <text y="-57" font-size="4" fill="#333" text-anchor="middle" font-family="Open Sans">Requirements</text>
    <text x="50" y="-22" font-size="3.8" fill="#333" font-family="Open Sans">Open-Ready</text>
    <text x="-68" y="-6" font-size="3.8" fill="#333" font-family="Open Sans">Products</text>
    <text x="32" y="38" font-size="3.6" fill="#333" font-family="Open Sans">Program Initiatives</text>
    <text x="32" y="43" font-size="3.6" fill="#333" font-family="Open Sans">Platforms/Systems</text>
    <text x="-40" y="58" font-size="4" fill="#333" font-family="Open Sans">Investment</text>
    <text x="-40" y="63" font-size="4" fill="#333" font-family="Open Sans">Decisions</text>
  </svg>
  <div class="foot"><i></i><i></i><i></i><span>Ideas to Reality 2014</span></div>
</section>

<section class="slide big" style="left:411px;top:250px">
  <h2 class="head">LINKING MULTIPLE <em>DATA POINTS</em></h2>
  <div class="blue">
    <div class="pointer" style="top:8px;width:18px;background:#fff"></div>
    <p class="lead" style="left:24px;top:4px;color:#fff;font-size:5.5px">All data points linked</p>
    <p class="tiny w" style="left:28px;top:12px">– Associated analysis of any or all data points<br>– Unrestricted analysis options and comparisons</p>
    <p class="lbl" style="left:18px;top:28px;width:50px">Locations</p>
    <p class="lbl" style="left:82px;top:28px;width:50px">Budget</p>
    <p class="lbl" style="left:146px;top:28px;width:50px">Strategy</p>
    <p class="lbl" style="left:210px;top:28px;width:50px">Reference</p>
    <p class="lbl" style="left:274px;top:28px;width:50px">Equipment</p>
    <div class="ph" role="img" aria-label="Map of locations" style="left:18px;top:34px;width:50px;height:28px;background:linear-gradient(135deg,#e9e1cf,#b8c9a8)"></div>
    <div class="ph" role="img" aria-label="Budget spreadsheet" style="left:82px;top:34px;width:50px;height:28px;background:linear-gradient(135deg,#f4efc8,#d8d3a0)"></div>
    <div class="ph dark" role="img" aria-label="Strategy document" style="left:146px;top:34px;width:50px;height:28px"></div>
    <div class="ph warm" role="img" aria-label="Reference image grid" style="left:210px;top:34px;width:50px;height:28px"></div>
    <div class="ph warm" role="img" aria-label="Equipment photo" style="left:274px;top:34px;width:50px;height:28px"></div>
    <svg style="position:absolute;left:0;top:0" width="368" height="162">
      <g stroke="#f2c7a4" stroke-width=".4" fill="none">
        <path d="M43 62 L30 92 M43 62 L85 92 M43 62 L140 92 M107 62 L60 92 M107 62 L170 92 M171 62 L115 92 M171 62 L225 92 M235 62 L195 92 M235 62 L280 92 M299 62 L250 92 M299 62 L335 92"/>
        <path d="M30 98 L45 118 M85 98 L110 118 M140 98 L170 118 M195 98 L236 118 M250 98 L300 118"/>
      </g>
      <line x1="10" y1="95" x2="358" y2="95" stroke="#fff" stroke-opacity=".5" stroke-width=".6"/>
    </svg>
    <span class="dot" style="left:12px;top:92px"></span><span class="dot" style="left:39px;top:92px"></span><span class="dot" style="left:66px;top:92px"></span><span class="dot" style="left:93px;top:92px"></span><span class="dot" style="left:120px;top:92px"></span><span class="dot" style="left:147px;top:92px"></span><span class="dot" style="left:174px;top:92px"></span><span class="dot" style="left:201px;top:92px"></span><span class="dot" style="left:228px;top:92px"></span><span class="dot" style="left:255px;top:92px"></span><span class="dot" style="left:282px;top:92px"></span><span class="dot" style="left:309px;top:92px"></span><span class="dot" style="left:336px;top:92px"></span>
    <div class="ph warm" role="img" aria-label="Organisation photo" style="left:20px;top:116px;width:50px;height:26px"></div>
    <div class="ph" role="img" aria-label="Standards document" style="left:84px;top:116px;width:50px;height:26px"></div>
    <div class="ph" role="img" aria-label="Doctrine pages" style="left:148px;top:112px;width:50px;height:30px"></div>
    <div class="ph dark" role="img" aria-label="Applications photo" style="left:212px;top:110px;width:50px;height:32px"></div>
    <div class="ph warm" role="img" aria-label="Training photo" style="left:276px;top:118px;width:50px;height:24px"></div>
    <p class="lbl" style="left:20px;top:144px;width:50px">Organizations</p>
    <p class="lbl" style="left:84px;top:144px;width:50px">Standards</p>
    <p class="lbl" style="left:148px;top:144px;width:50px">Doctrine</p>
    <p class="lbl" style="left:212px;top:144px;width:50px">Applications</p>
    <p class="lbl" style="left:276px;top:144px;width:50px">Training</p>
  </div>
  <div class="foot"><i></i><i></i><i></i><span>Ideas to Reality 2014</span></div>
</section>

<section class="slide big" style="left:796px;top:250px">
  <h2 class="head">K48 DISCOVERY PLATFORM</h2>
  <div class="pointer" style="top:46px;width:30px"></div>
  <p class="lead" style="left:36px;top:42px;font-size:5.5px;font-weight:600">MULTI-DEVICE, <span class="o">MOBILE</span> and <span class="o">DESKTOP</span> Ready!</p>
  <div class="ph device" role="img" aria-label="Desktop monitor and phone showing a dashboard with map, bar chart and pie chart" style="left:26px;top:60px;width:172px;height:116px"></div>
  <div class="row" style="top:34px"><b>01</b>MODULAR TOOL ARCHITECTURE</div>
  <div class="row" style="top:47px"><b>02</b>EXTENSIBLE MODULE FRAMEWORK</div>
  <div class="row" style="top:60px"><b>03</b>REAL TIME DATA EVENTS</div>
  <div class="row" style="top:73px"><b>04</b>SEMANTIC &amp; CONCEPT</div>
  <div class="row sub" style="top:86px"><b>a</b>Searching</div>
  <div class="row" style="top:99px"><b>05</b>ENTITY &amp; FACET SEARCHING</div>
  <div class="row" style="top:112px"><b>06</b>USER UPDATEABLE DATA</div>
  <div class="row sub" style="top:125px"><b>a</b>Other</div>
  <div class="foot"><i></i><i></i><i></i><span>Ideas to Reality 2014</span></div>
</section>

<!-- Row 3 -->
<section class="slide big" style="left:26px;top:474px">
  <h2 class="head">NTA <em>DASHBOARD</em> INIATIVE</h2>
  <div class="blue">
    <div class="ph dark" role="img" aria-label="Dashboard home screen with globe" style="left:6px;top:6px;width:88px;height:34px;background:linear-gradient(135deg,#1d3f6e,#4f87b8)"></div>
    <div class="ph" role="img" aria-label="Agency table screen" style="left:6px;top:46px;width:88px;height:40px;background:linear-gradient(135deg,#f2f4f6,#c9d2da)"></div>
    <div class="ph" role="img" aria-label="Status grid screen" style="left:100px;top:58px;width:60px;height:30px;background:linear-gradient(135deg,#f0f0f0,#cfe3c6)"></div>
    <div class="ph" role="img" aria-label="Gauge screen" style="left:166px;top:58px;width:60px;height:30px;background:linear-gradient(135deg,#f2f2f2,#f4c9a0)"></div>
    <div class="ph" role="img" aria-label="Pie chart screen" style="left:232px;top:58px;width:60px;height:30px;background:linear-gradient(135deg,#f5f5f5,#c7e6c2)"></div>
    <div class="ph" role="img" aria-label="Workflow detail screen" style="left:6px;top:92px;width:88px;height:64px;background:linear-gradient(135deg,#f4f4f4,#c6d0da)"></div>
    <ul class="list w" style="left:104px;top:6px;width:110px;font-size:3.8px;line-height:5px">
      <li>Provides a 1 stop interactive display to address the health of the agency</li>
      <li style="margin-top:3px">Facilitates decision making with drill down to greater levels of detail at a click</li>
    </ul>
    <p class="tiny w" style="left:222px;top:6px;width:120px;font-size:3.8px;line-height:5px">Uses business rules supported by an Enterprise Scoring System to provide near real time update of agency health</p>
    <p class="tiny w" style="left:104px;top:104px;width:110px;font-size:3.8px;line-height:5px">• Fosters automated system to system interaction to gain copy authoritative data providing the most current data available</p>
    <p class="tiny w" style="left:222px;top:104px;width:120px;font-size:3.8px;line-height:5px">Supports NTA executives with plans to provide dashboards down to the supervisor level</p>
  </div>
  <div class="foot"><i></i><i></i><i></i><span>Ideas to Reality 2014</span></div>
</section>

<section class="slide big" style="left:411px;top:474px">
  <h2 class="head">SYSTEM <em>BENEFITS</em></h2>
  <div class="pointer" style="top:46px;width:20px"></div>
  <p class="lead" style="left:26px;top:42px">YOUR <span class="o">TITLE</span></p>
  <ul class="list" style="left:40px;top:60px;width:150px;line-height:6.4px">
    <li>All Scale Document → Entity Analysis Platform</li>
    <li>Convert Unstructured Multi-lingual Text into Insights</li>
    <li>Simple, Intuitive Search Analytics</li>
    <li>From Data Mining to Entity Mining</li>
    <li>Automatic Link Analysis &amp; Databasing</li>
  </ul>
  <p class="tiny" style="left:40px;top:100px;width:140px">Sed ut perspiciatis unde omnis iste natus error sit voluptatem accusantium doloremque laudantium, totam rem aperiam, eaque ipsa quae ab illo inventore veritatis et quasi architecto beatae vitae dicta sunt explicabo.</p>
  <p class="note" style="left:40px;top:128px;width:140px">Nemo enim ipsam voluptatem quia voluptas sit aspernatur aut odit aut fugit, sed quia consequuntur magni dolores.</p>
  <svg style="position:absolute;left:196px;top:48px" width="152" height="104" viewBox="0 0 150 100">
    <g stroke="#fff" stroke-width="1">
      <polygon points="75,0 90,20 60,20" fill="#f47a30"/>
      <polygon points="60,20 90,20 105,40 45,40" fill="#8cc0d8"/>
      <polygon points="45,40 105,40 120,60 30,60" fill="#5a8fb0"/>
      <polygon points="30,60 120,60 135,80 15,80" fill="#3f6f93"/>
      <polygon points="15,80 135,80 150,100 0,100" fill="#2c4a6e"/>
    </g>
    <g font-family="Open Sans" font-size="4" fill="#fff" text-anchor="middle">
      <text x="75" y="16">Insight</text><text x="75" y="32">Intelligence</text><text x="75" y="52">Knowledge</text><text x="75" y="72">Information</text><text x="75" y="92">Data</text>
    </g>
  </svg>
  <div class="foot"><i></i><i></i><i></i><span>Ideas to Reality 2014</span></div>
</section>

<section class="slide big" style="left:796px;top:474px">
  <h2 class="head">REALISED <em>BENIFITS</em></h2>
  <div class="blue" style="right:194px">
    <div class="ph device" role="img" aria-label="Desktop monitor showing a dashboard with map, bar chart and pie chart" style="left:20px;top:14px;width:134px;height:96px"></div>
    <p class="note" style="left:10px;top:124px;width:150px">Lorem ipsum dolor sit amet, consectetur adipiscing elit, sed do eiusmod tempor incididunt ut labore.</p>
  </div>
  <ul class="list" style="left:182px;top:36px;width:176px;font-size:3.6px;line-height:5px">
    <li>Identified the need to create a common taxonomy</li>
    <li style="padding-left:8px" class="s">Allowing for simplified data association</li>
    <li>Significantly reduced data call response time for budget and congressional inquiries</li>
    <li style="padding-left:8px" class="s">Required data compiled rapidly and accurately in response</li>
    <li>Assisted in plans alignment to the most current guidance and requirements</li>
    <li style="padding-left:8px" class="s">Annual guidance updates seamlessly result in plan alignment</li>
    <li>Provided integrated analysis of the systems, requirements and products data</li>
    <li>Aligned budget data with production data allowing for cost analysis</li>
    <li>Savings in personnel research and compilation hours</li>
  </ul>
  <div class="foot"><i></i><i></i><i></i><span>Ideas to Reality 2014</span></div>
</section>

<div class="band"></div>

<!-- Bottom row 1 -->
<section class="slide small" style="left:26px;top:746px">
  <h2 class="head">DEVELOPMENT <em>TIMELINE</em></h2>
  <svg style="position:absolute;left:0;top:28px" width="262" height="46">
    <line x1="6" y1="18" x2="256" y2="18" stroke="#7fb5cf" stroke-width="1"/>
    <g font-family="Open Sans" font-size="3.6" fill="#fff" text-anchor="middle">
      <rect x="22" y="4" width="18" height="7" fill="#5fa3c4"/><text x="31" y="9">Phase 1</text>
      <rect x="40" y="24" width="18" height="7" fill="#2c4a6e"/><text x="49" y="29">Phase 2</text>
      <rect x="72" y="4" width="18" height="7" fill="#f47a30"/><text x="81" y="9">Phase 3</text>
      <rect x="98" y="28" width="18" height="7" fill="#2c4a6e"/><text x="107" y="33">Phase 4</text>
      <rect x="128" y="4" width="18" height="7" fill="#5fa3c4"/><text x="137" y="9">Phase 5</text>
      <rect x="186" y="4" width="18" height="7" fill="#5fa3c4"/><text x="195" y="9">Phase 6</text>
      <rect x="198" y="28" width="18" height="7" fill="#f47a30"/><text x="207" y="33">Phase 7</text>
    </g>
    <g stroke="#2c4a6e" stroke-width=".5"><line x1="31" y1="11" x2="31" y2="18"/><line x1="49" y1="18" x2="49" y2="24"/><line x1="81" y1="11" x2="81" y2="18"/><line x1="107" y1="18" x2="107" y2="28"/><line x1="137" y1="11" x2="137" y2="18"/><line x1="195" y1="11" x2="195" y2="18"/><line x1="207" y1="18" x2="207" y2="28"/></g>
  </svg>
  <div style="position:absolute;left:0;right:0;top:74px;height:10px;background:linear-gradient(90deg,#e6f1f6,#c9e1ec,#e6f1f6)"></div>
  <p class="tiny" style="left:12px;top:90px;width:36px">PHASE 1<br>Lorem ipsum dolor sit amet elit.</p>
  <p class="tiny" style="left:52px;top:90px;width:36px">PHASE 2<br>Lorem ipsum dolor sit amet elit.</p>
  <p class="tiny" style="left:92px;top:90px;width:36px">PHASE 3<br>Lorem ipsum dolor sit amet elit.</p>
  <p class="tiny" style="left:132px;top:90px;width:36px">PHASE 4<br>Lorem ipsum dolor sit amet elit.</p>
  <p class="tiny" style="left:172px;top:90px;width:36px">PHASE 5<br>Lorem ipsum dolor sit amet elit.</p>
  <p class="tiny" style="left:212px;top:90px;width:36px">PHASE 6<br>Lorem ipsum dolor sit amet elit.</p>
  <div class="foot"><i></i><i></i><i></i><span>Ideas to Reality 2014</span></div>
</section>

<section class="slide small" style="left:330px;top:746px">
  <h2 class="head">CHARTS <em>EXAMPLES</em></h2>
  <div style="position:absolute;left:28px;top:28px;width:38px;height:14px;background:var(--sky);color:#fff;font-size:8px;line-height:14px;padding-left:3px">60%</div>
  <p class="tiny" style="left:28px;top:46px;width:40px">Lorem ipsum dolor sit amet, consectetur elit.</p>
  <div style="position:absolute;left:28px;top:108px;width:38px;height:14px;background:var(--navy);color:#fff;font-size:8px;line-height:14px;padding-left:3px">40%</div>
  <p class="tiny" style="left:72px;top:108px;width:40px">Lorem ipsum dolor sit amet, consectetur elit.</p>
  <svg style="position:absolute;left:16px;top:35px" width="80" height="80"><path d="M12 6 H70 M12 80 V6" stroke="#999" stroke-width=".5" fill="none"/></svg>
  <div style="position:absolute;left:82px;top:56px;width:38px;height:38px;border-radius:50%;background:conic-gradient(var(--sky) 0 60%,var(--navy) 0)"></div>
  <div style="position:absolute;left:87px;top:61px;width:28px;height:28px;border-radius:50%;background:#fff;font-size:4px;text-align:center;line-height:28px;color:#555">40%&nbsp;–&nbsp;60%</div>
  <p style="position:absolute;left:146px;top:40px;font-size:4.5px;color:#444">SIMPLE PROJECT #1</p>
  <p class="tiny" style="left:146px;top:48px;width:96px">Lorem ipsum dolor sit amet, consectetur adipiscing elit, sed do eiusmod tempor incididunt ut labore et dolore magna aliqua.</p>
  <p class="tiny" style="left:146px;top:66px;width:96px">Ut enim ad minim veniam, quis nostrud exercitation ullamco laboris nisi ut aliquip ex ea commodo consequat duis aute irure dolor.</p>
  <p class="note" style="left:146px;top:118px;width:96px">Lorem ipsum dolor sit amet, consectetur adipiscing.</p>
  <div class="foot"><i></i><i></i><i></i><span>Ideas to Reality 2014</span></div>
</section>

<section class="slide small" style="left:620px;top:746px">
  <h2 class="head">OUR <em>ENGINEERS</em></h2>
  <div class="circ" style="left:56px;top:26px;width:34px;height:34px;background:#3a4a5c;font-size:3.6px">ENGINEER NAME</div>
  <div class="circ" style="left:132px;top:82px;width:34px;height:34px;background:#3a4a5c;font-size:3.6px">ENGINEER NAME</div>
  <svg style="position:absolute;left:0;top:0" width="262" height="148">
    <g stroke="#888" stroke-width=".4"><line x1="8" y1="43" x2="56" y2="43"/><line x1="90" y1="43" x2="230" y2="43"/><line x1="30" y1="99" x2="132" y2="99"/><line x1="166" y1="99" x2="250" y2="99"/></g>
    <g font-family="Open Sans" font-size="3.2" fill="#666"><text x="8" y="39">Lorem ipsum dolor</text><text x="168" y="96">Lorem ipsum dolor</text><text x="98" y="28">SKILLS</text><text x="30" y="84">GENERAL SKILLS</text></g>
    <g fill="#2c4a6e"><rect x="98" y="31" width="58" height="3.5"/><rect x="98" y="36" width="48" height="3.5" fill="#4a7fa0"/><rect x="98" y="46" width="64" height="3.5"/><rect x="98" y="51" width="40" height="3.5" fill="#4a7fa0"/></g>
    <g fill="#2c4a6e"><rect x="30" y="87" width="70" height="3.5"/><rect x="30" y="92" width="52" height="3.5" fill="#4a7fa0"/><rect x="30" y="102" width="60" height="3.5"/><rect x="30" y="107" width="44" height="3.5" fill="#4a7fa0"/></g>
    <g font-family="Open Sans" font-size="3" fill="#888"><text x="160" y="34">80%</text><text x="166" y="49">90%</text><text x="104" y="90">75%</text><text x="94" y="105">65%</text></g>
  </svg>
  <div class="foot"><i></i><i></i><i></i><span>Ideas to Reality 2014</span></div>
</section>

<section class="slide small" style="left:910px;top:746px">
  <div class="ph" role="img" aria-label="Street map of the office area" style="left:0;top:0;width:128px;height:139px;background:linear-gradient(135deg,#e6e6e6,#c8c8c8)"></div>
  <svg style="position:absolute;left:58px;top:46px" width="12" height="16" viewBox="0 0 12 16"><path d="M6 0a6 6 0 0 1 6 6c0 4-6 10-6 10S0 10 0 6a6 6 0 0 1 6-6z" fill="#f47a30"/><circle cx="6" cy="6" r="2.2" fill="#fff"/></svg>
  <p style="position:absolute;left:140px;top:8px;font-size:6.5px;color:var(--navy)">GET IN <span class="s">CONTACT</span></p>
  <ul style="position:absolute;left:150px;top:34px;list-style:none;font-size:3.6px;line-height:7px;color:#666">
    <li><span style="display:inline-block;width:3px;height:3px;background:var(--steel);margin-right:4px"></span>+1 (555) 014-2290</li>
    <li><span style="display:inline-block;width:3px;height:3px;background:var(--steel);margin-right:4px"></span>+1 (555) 014-2291</li>
    <li><span style="display:inline-block;width:3px;height:3px;background:var(--steel);margin-right:4px"></span>info@k48group.com</li>
    <li><span style="display:inline-block;width:3px;height:3px;background:var(--steel);margin-right:4px"></span>www.k48group.com</li>
    <li><span style="display:inline-block;width:3px;height:3px;background:var(--steel);margin-right:4px"></span>120 Harbor Lane, Riverton</li>
  </ul>
  <p style="position:absolute;left:140px;top:101px;font-size:3.6px;color:var(--orange)">COMPANY NAME</p>
  <div style="position:absolute;left:140px;top:107px;width:112px;height:18px;background:#5d6570"><span style="position:absolute;left:0;top:0;width:16px;height:18px;background:var(--orange)"></span><span style="position:absolute;left:20px;top:0;font-size:3.4px;line-height:18px;color:#fff">120 Harbor Lane, Riverton</span></div>
  <div class="foot"><i></i><i></i><i></i><span>Ideas to Reality 2014</span></div>
</section>

<!-- Bottom row 2 -->
<section class="slide small" style="left:26px;top:922px;width:266px;height:150px;background:linear-gradient(180deg,#25466a 0%,#5c8fb1 55%,#2c4a6e 100%)">
  <div class="circ" style="left:6px;top:26px;width:96px;height:96px;background:#2c4a6e;font-size:10px;font-weight:300">COFFEE BREAK</div>
  <div class="circ" style="left:100px;top:60px;width:24px;height:24px;background:#6aaecb">
    <svg width="12" height="10" viewBox="0 0 12 10"><path d="M1 1h8v5a3 3 0 0 1-3 3H4a3 3 0 0 1-3-3z" fill="#fff"/><path d="M9 2h1.5a1.5 1.5 0 0 1 0 3H9" stroke="#fff" fill="none"/></svg>
  </div>
  <div class="circ" style="left:132px;top:58px;width:28px;height:28px;background:var(--orange);font-size:3.6px">11:00 – 11:30</div>
  <div class="circ" style="left:168px;top:60px;width:24px;height:24px;background:#6aaecb">
    <svg width="12" height="12" viewBox="0 0 12 12"><circle cx="6" cy="6" r="5" stroke="#fff" stroke-width="1.2" fill="none"/><path d="M6 3v3l2 1.5" stroke="#fff" fill="none"/></svg>
  </div>
</section>

<section class="slide small" style="left:330px;top:922px;height:150px">
  <h2 class="head">YOUR <em>TITLE</em></h2>
  <div class="circ" style="left:53px;top:30px;width:12px;height:12px;background:var(--steel)"></div>
  <div class="circ" style="left:125px;top:30px;width:12px;height:12px;background:var(--steel)"></div>
  <div class="circ" style="left:197px;top:30px;width:12px;height:12px;background:var(--steel)"></div>
  <p style="position:absolute;left:28px;top:46px;width:62px;text-align:center;font-size:4px;color:var(--orange)">YOUR TITLE #1</p>
  <p style="position:absolute;left:100px;top:46px;width:62px;text-align:center;font-size:4px;color:var(--orange)">YOUR TITLE #2</p>
  <p style="position:absolute;left:172px;top:46px;width:62px;text-align:center;font-size:4px;color:var(--orange)">YOUR TITLE #3</p>
  <p class="tiny" style="left:28px;top:56px;width:62px">Lorem ipsum dolor sit amet, consectetur adipiscing elit, sed do eiusmod tempor incididunt ut labore et dolore magna aliqua enim.</p>
  <p class="tiny" style="left:100px;top:56px;width:62px">Lorem ipsum dolor sit amet, consectetur adipiscing elit, sed do eiusmod tempor incididunt ut labore et dolore magna aliqua enim.</p>
  <p class="tiny" style="left:172px;top:56px;width:62px">Lorem ipsum dolor sit amet, consectetur adipiscing elit, sed do eiusmod tempor incididunt ut labore et dolore magna aliqua enim.</p>
  <div class="foot"><i></i><i></i><i></i><span>Ideas to Reality 2014</span></div>
</section>

<section class="slide small" style="left:620px;top:922px;height:150px;background:linear-gradient(180deg,#2e5377 0%,#6a9fbf 50%,#2c4a6e 100%)">
  <div class="circ" style="left:10px;top:98px;width:44px;height:44px;background:#2c4a6e"></div>
  <div class="circ" style="left:44px;top:30px;width:42px;height:42px;background:var(--orange);font-size:6px">THANKS</div>
  <div class="circ" style="left:100px;top:76px;width:22px;height:22px;background:var(--orange);font-size:5px">FOR</div>
  <div class="circ" style="left:152px;top:44px;width:48px;height:48px;background:var(--orange);font-size:6px">WATCHING</div>
  <div class="circ" style="left:112px;top:22px;width:20px;height:20px;background:#7fc0dc"></div>
  <div class="circ" style="left:196px;top:14px;width:30px;height:30px;background:#2c4a6e"></div>
  <div class="circ" style="left:208px;top:98px;width:10px;height:10px;background:#7fc0dc"></div>
</section>

<div class="brand">
  <span class="mark"></span>
  <span class="name">K48</span>
</div>

</body>
</html>
```